Marijuana Lifestyle Multi-Shop Brand Website

We need a website that provides an online retail shop for our products, along with the additional functionality:

Main Page: Slider with great photography (we are still looking for a professional photographer to take photos for us.

Shop Tab: E-commerce site.
- Main Categories:
- Accessories
- Bubblers
- Dry Pieces
- Scientific Glass
- Water Pipes
- Custom Shop
- University Store

Stores/Resellers: This is a store look-up, so people can enter their zipcode and find our resellers and partners.

Brand Partners: Just a basic filter and page so that we can highlight our partners and why we've selected them.

Contact Us: Basic Form
- Career Page: Basic Page

About Us: Basic Page

Blog:

Search Bar:

Essentially, we want a near exact copy of this website, but with our brand, logo and content. https://plumcratevault.com/

This site is really really simple, but we like simple.

Our reserved domain address is: www.runsowmend.com

About Us:
We are multi-shop for marijuana-related accessories. We sell quality glass pipes, vaporizers, amazing storage options, dime bags, custom t-shirts and other stuff.

We have a network of resellers that allow us to put in micro-installations into gift shops, convenience stores, tobacco stores, etc. and we are trying to change the overall perception that buying these items should be mainstream and as transparent as going to the Elk or the Birch Depot.

I've attached a logo that should give you an idea of our color scheme. We don't have our photography yet for the slider

As an FYI, for the e-commerce part of my website, I already have a license for WP SwiftTill.

```html
<!DOCTYPE html>
<html lang="en">
<head>
<meta charset="utf-8">
<title>Contact Us – fernhollow</title>
<link rel="stylesheet" href="https://fonts.googleapis.com/css2?family=Rokkitt:wght@400;500&family=PT+Sans&display=swap">
<style>
:root{
  --cream:#f6f9e3;
  --forest:#354503;
  --forest-deep:#2f3c04;
  --field-border:#c9d2a3;
  --ink:#1f2410;
  --dots:#3d4d0a;
  --map-base:#efefe9;
  --map-green:#cfe0b4;
  --white:#ffffff;
}
*{box-sizing:border-box;margin:0;padding:0}
html,body{width:1143px;height:1200px;overflow:hidden;background:var(--white)}
body{position:relative;font-family:"PT Sans",sans-serif;color:var(--ink)}
.site-header{position:absolute;left:0;top:0;width:1143px;height:223px;background:var(--cream);box-shadow:0 2px 3px rgba(0,0,0,.25)}
.brand{position:absolute;left:0;top:80px;width:1143px;display:flex;justify-content:center;align-items:center;gap:12px}
.brand-dot{width:26px;height:26px;border-radius:50%;background:var(--forest)}
.brand-name{font-family:"Rokkitt",serif;font-size:44px;font-weight:500;color:var(--forest);letter-spacing:1px}
.main-nav a{position:absolute;top:191px;height:32px;line-height:26px;font-family:"Rokkitt",serif;font-size:15px;color:var(--forest);text-decoration:none;letter-spacing:.6px}
.main-nav .is-active{background:var(--forest);color:var(--cream);border-radius:5px 5px 0 0;text-align:center;width:93px}
.search-icon{position:absolute;left:871px;top:198px}
.page-title{position:absolute;left:261px;top:244px;font-family:"Rokkitt",serif;font-weight:400;font-size:33px;color:var(--forest);letter-spacing:1px}
.dots{position:absolute;height:3px;background:radial-gradient(circle,var(--dots) 1.2px,transparent 1.5px) 0 0/6px 3px repeat-x}
.title-rule{left:261px;top:303px;width:622px}
.map-area{position:absolute;left:0;top:336px;width:1143px;height:331px;border:1px solid #b9b9b2;background:linear-gradient(135deg,var(--map-base) 0%,#e9eedd 40%,var(--map-green) 60%,var(--map-base) 80%,#dfe8cd 100%)}
.form-label{position:absolute;left:261px;font-family:"Rokkitt",serif;font-size:19px;color:var(--forest);letter-spacing:.6px}
.field{position:absolute;left:262px;width:319px;background:var(--cream);border:1px solid var(--field-border);border-radius:4px}
.info-heading{position:absolute;left:628px;font-family:"Rokkitt",serif;font-size:19px;color:var(--forest);letter-spacing:.6px}
.hours{position:absolute;left:629px;top:717px;font-size:12.5px;line-height:14.5px}
.info-rule{left:629px;top:773px;width:243px}
.contact-line{position:absolute;left:669px;font-size:12.5px;line-height:14px}
.icon{position:absolute}
.site-footer{position:absolute;left:0;top:1149px;width:1143px;height:51px;background:var(--forest);border-top:2px solid #c8ccbd}
.copyright{position:absolute;left:231px;top:18px;font-family:"Rokkitt",serif;font-size:9.5px;color:#d6dcb6;letter-spacing:.6px}
.social{position:absolute;top:18px;width:14px;height:14px;border-radius:50%;border:1.5px solid #bfc6a0}
</style>
</head>
<body>
<header class="site-header">
  <div class="brand"><span class="brand-dot"></span><span class="brand-name">fernhollow</span></div>
  <nav class="main-nav">
    <a style="left:261px">Home</a>
    <a style="left:330px">Shop</a>
    <a style="left:394px">Resellers</a>
    <a style="left:485px">Brand Partners</a>
    <a class="is-active" style="left:602px">Contact Us</a>
    <a style="left:717px">About Us</a>
    <a style="left:809px">Blog</a>
  </nav>
  <svg class="search-icon" width="11" height="11" viewBox="0 0 11 11"><circle cx="4.5" cy="4.5" r="3.2" fill="none" stroke="#354503" stroke-width="1.6"/><line x1="7" y1="7" x2="10" y2="10" stroke="#354503" stroke-width="1.8"/></svg>
</header>

<h1 class="page-title">Contact Us</h1>
<div class="dots title-rule"></div>

<div class="map-area" role="img" aria-label="Road map of the central and western United States with three store location pins"></div>

<label class="form-label" style="top:690px">Your name</label>
<div class="field" style="top:724px;height:39px"></div>
<label class="form-label" style="top:786px">Your e-mail address</label>
<div class="field" style="top:820px;height:39px"></div>
<label class="form-label" style="top:882px">Subject</label>
<div class="field" style="top:916px;height:39px"></div>
<label class="form-label" style="top:978px">Message</label>
<div class="field" style="top:1012px;height:107px"></div>

<h2 class="info-heading" style="top:690px;font-weight:400">Business hour</h2>
<p class="hours">Monday - Friday : 9am - 6pm<br>Saturday - Sunday : Closed</p>
<div class="dots info-rule"></div>
<h2 class="info-heading" style="top:800px;font-weight:400">Our office</h2>

<svg class="icon" style="left:629px;top:832px" width="22" height="28" viewBox="0 0 22 28"><path d="M11 1C5.5 1 1.5 5 1.5 10.3 1.5 17 11 27 11 27s9.5-10 9.5-16.7C20.5 5 16.5 1 11 1z" fill="#354503"/><circle cx="11" cy="10.3" r="4.6" fill="#fff"/></svg>
<p class="contact-line" style="top:834px">27 Fernhollow Lane, Millbrook,<br>United States</p>

<svg class="icon" style="left:629px;top:876px" width="16" height="28" viewBox="0 0 16 28"><rect x="0" y="0" width="16" height="28" rx="2" fill="#354503"/><rect x="2.5" y="4" width="11" height="17" fill="#fff"/></svg>
<p class="contact-line" style="top:883px">(555) 0142 7736</p>

<svg class="icon" style="left:629px;top:926px" width="26" height="17" viewBox="0 0 26 17"><rect x="1" y="1" width="24" height="15" fill="none" stroke="#354503" stroke-width="2"/><path d="M1 1l12 9 12-9M1 16l9-7M25 16l-9-7" fill="none" stroke="#354503" stroke-width="2"/></svg>
<p class="contact-line" style="top:927px">hello@fernhollow.example</p>

<footer class="site-footer">
  <p class="copyright">fernhollow Copyright &nbsp;© 2014. All Rights Reserved.</p>
  <span class="social" style="left:754px"></span>
  <span class="social" style="left:782px"></span>
  <span class="social" style="left:810px"></span>
  <span class="social" style="left:839px"></span>
  <span class="social" style="left:868px"></span>
</footer>
</body>
</html>
```